Love pets? Create a veterinary business card that aligns with our new revamped website.

Greetings! We are a five-doctor veterinary hospital that seeks your expertise in designing a new business card that harmonizes with our recently revitalized website: www.tqrn.net. The card should feature our logo, the five doctors, operating hours, contact information, and communicate our purpose and personality.

Contact Information for Business Card

TBA

```html
<!DOCTYPE html>
<html lang="en">
<head>
<meta charset="utf-8">
<title>Maple Hollow Veterinary Hospital – Business Card</title>
<link rel="stylesheet" href="https://fonts.googleapis.com/css2?family=Quicksand:wght@500;600;700&family=Dancing+Script:wght@700&display=swap">
<style>
  :root {
    --page-bg: #e9e7e3;
    --green-dark: #1d5a17;
    --green-mid: #2f7f29;
    --green-light: #4f9a45;
    --brand-green: #3a8a2e;
    --accent-orange: #c4862a;
    --text-grey: #555a5e;
    --rule-grey: #9a9f9c;
    --card-white: #ffffff;
    --white: #ffffff;
  }
  * { box-sizing: border-box; margin: 0; padding: 0; }
  html, body {
    width: 1200px; height: 900px; overflow: hidden;
    background: var(--page-bg);
    font-family: "Quicksand", sans-serif;
  }
  .canvas { position: relative; width: 1200px; height: 900px; }

  .card {
    position: absolute; left: 250px; width: 700px; height: 400px;
    border-radius: 0 30px 0 30px;
    overflow: hidden;
    box-shadow: 0 8px 24px rgba(0,0,0,.18);
  }

  /* Front */
  .card--front {
    top: 30px;
    background: radial-gradient(ellipse at 40% 55%, var(--green-light) 0%, var(--green-mid) 45%, var(--green-dark) 100%);
    color: var(--white);
  }
  .front-brand { position: absolute; left: 60px; top: 110px; display: flex; align-items: center; gap: 18px; }
  .brand-dot { width: 58px; height: 58px; border-radius: 50%; background: var(--white); }
  .front-brand .brand-name { font-size: 44px; font-weight: 700; color: var(--white); }
  .front-rule { position: absolute; left: 60px; right: 60px; top: 200px; border-top: 1.5px solid rgba(255,255,255,.8); }
  .vision { position: absolute; left: 60px; top: 218px; font-size: 25px; font-weight: 600; }
  .values { position: absolute; left: 84px; top: 262px; font-size: 23px; font-weight: 600; line-height: 1.45; }
  .values .sep { display: inline-block; width: 7px; height: 7px; border-radius: 50%; background: var(--white); margin: 0 8px; vertical-align: middle; }

  /* Back */
  .card--back { top: 470px; background: var(--card-white); color: var(--text-grey); }
  .doctor { position: absolute; left: 50px; top: 40px; }
  .doctor-name { font-family: "Dancing Script", cursive; font-size: 46px; color: var(--accent-orange); }
  .doctor-cred { font-size: 22px; font-weight: 600; color: var(--text-grey); margin-left: 4px; }
  .doctor-title { font-size: 21px; font-weight: 600; margin-top: 2px; }

  .contact { position: absolute; left: 60px; top: 165px; display: flex; gap: 18px; }
  .contact-col { display: flex; flex-direction: column; gap: 8px; font-size: 21px; font-weight: 600; }
  .contact-col--web { padding-left: 18px; border-left: 1.5px solid var(--brand-green); font-size: 19px; }
  .contact-line { display: flex; align-items: center; gap: 10px; }
  .icon { width: 20px; height: 20px; flex: none; }

  .location { position: absolute; right: 44px; top: 40px; text-align: right; font-size: 20px; font-weight: 600; line-height: 1.35; }
  .hours-title { font-size: 23px; font-weight: 700; color: var(--brand-green); margin-top: 14px; }

  .back-rule { position: absolute; left: 50px; right: 50px; top: 268px; border-top: 1.5px solid var(--rule-grey); }
  .back-brand { position: absolute; left: 60px; top: 298px; display: flex; align-items: center; gap: 16px; }
  .back-brand .brand-dot { width: 54px; height: 54px; background: var(--brand-green); }
  .back-brand .brand-name { font-size: 42px; font-weight: 700; color: var(--brand-green); }
</style>
</head>
<body>
<main class="canvas">

  <section class="card card--front" aria-label="Card front">
    <div class="front-brand">
      <span class="brand-dot"></span>
      <span class="brand-name">Maple Hollow</span>
    </div>
    <div class="front-rule"></div>
    <p class="vision">Our Vision: To Be the Best Veterinary Hospital</p>
    <p class="values">
      Compassionate Quality Care<br>
      Education<span class="sep"></span>Fear Free<br>
      Integrity<span class="sep"></span>Trust
    </p>
  </section>

  <section class="card card--back" aria-label="Card back">
    <div class="doctor">
      <span class="doctor-name">Dan Whitmore,</span><span class="doctor-cred">DVM</span>
      <p class="doctor-title">Associate Veterinarian</p>
    </div>

    <div class="contact">
      <div class="contact-col">
        <span class="contact-line">
          <svg class="icon" viewBox="0 0 24 24" aria-hidden="true"><path fill="#c4862a" d="M6.6 10.8a15 15 0 0 0 6.6 6.6l2.2-2.2a1 1 0 0 1 1-.25 11.4 11.4 0 0 0 3.6.57 1 1 0 0 1 1 1V20a1 1 0 0 1-1 1A17 17 0 0 1 3 4a1 1 0 0 1 1-1h3.5a1 1 0 0 1 1 1c0 1.25.2 2.45.57 3.57a1 1 0 0 1-.25 1z"/></svg>
          (555) 204-3817
        </span>
        <span class="contact-line">
          <svg class="icon" viewBox="0 0 24 24" aria-hidden="true"><path fill="#c4862a" d="M6 2h9l3 3v4H6zM4 10h16a2 2 0 0 1 2 2v6h-4v4H6v-4H2v-6a2 2 0 0 1 2-2zm4 6v4h8v-4z"/></svg>
          (555) 204-3900
        </span>
      </div>
      <div class="contact-col contact-col--web">
        <span class="contact-line">
          <svg class="icon" viewBox="0 0 24 24" aria-hidden="true"><path fill="#c4862a" d="M3 5h18a1 1 0 0 1 1 1v12a1 1 0 0 1-1 1H3a1 1 0 0 1-1-1V6a1 1 0 0 1 1-1zm0 2v.5l9 5.5 9-5.5V7l-9 5.5z"/></svg>
          info@tqrn.net
        </span>
        <span class="contact-line">
          <svg class="icon" viewBox="0 0 24 24" aria-hidden="true"><circle cx="12" cy="12" r="9" fill="none" stroke="#c4862a" stroke-width="2"/><path d="M3 12h18M12 3c3 3 3 15 0 18M12 3c-3 3-3 15 0 18" fill="none" stroke="#c4862a" stroke-width="1.6"/></svg>
          www.tqrn.net
        </span>
      </div>
    </div>

    <div class="location">
      <p>4820 Cedar Ridge Road<br>Millbrook, TX 75099</p>
      <p class="hours-title">HOSPITAL HOURS</p>
      <p>Mon-Friday 7-6<br>Sat 8-12, Sun Closed</p>
    </div>

    <div class="back-rule"></div>
    <div class="back-brand">
      <span class="brand-dot"></span>
      <span class="brand-name">Maple Hollow</span>
    </div>
  </section>

</main>
</body>
</html>
```